Emerging Australian photographer

I'm based in Cunderdin, a small rural town in the Wheatbelt area of Western Australia. So its a good thing that I love to travel further afield both for pleasure and for work. To me that is one and the same thing in any event!

My desire is to take photos that make the viewers heart skip. I love taking photos of people doing the things they love or being with the people they love. For me, the joy of photography comes with capturing the 'moments between the moments'. I like candid photography best of all - like when the new husband is staring joyfully at his bride and at that minute is unaware of the photographer capturing the moment.

I am available for weddings, engagements, birthdays, special events, newborns, family or individual portraits. By the end of the year I will be accredited with the Coastal Guild of Image Artisans.

I need a card that stands out but is elegant and would sit well on the table at a wedding or be given out in the church grounds. Classy and a little bit sassy.

Target Market(s)

Consumers who are seeking photographic services, eg wedding guests who see me at work and make enquiries.

Industry/Entity Type

Church

Contact Information for Business Card

Tamsin Bexley Photography
Tamsin Bexley
0452 307 618
www.tamsinbexley.com.au
photos@tamsinbexley.com.au

Requirements
Must have
• Must fit with the theme in the watermarks, but be crisp and modern.
Nice to have
• However it's not essential to have the pink! Facebook and Twitter logos.
Should not have
• Old style fonts like times new roman.

```html
<!DOCTYPE html>
<html lang="en">
<head>
<meta charset="utf-8">
<title>Tamsin Bexley Photography – Business Card</title>
<link href="https://fonts.googleapis.com/css2?family=Advent+Pro:wght@200&family=Didact+Gothic&display=swap" rel="stylesheet">
<style>
  :root {
    --backdrop: #6b2a1c;
    --card-black: #000000;
    --blush: #e9b7c9;
    --white: #ffffff;
    --band-text: #4a4a4a;
    --shadow: rgba(0,0,0,0.45);
  }
  html, body {
    margin: 0;
    padding: 0;
    width: 1200px;
    height: 927px;
    overflow: hidden;
    background: var(--backdrop);
  }
  .canvas {
    position: relative;
    width: 1200px;
    height: 927px;
  }
  .card {
    position: absolute;
    width: 540px;
    height: 330px;
    background: var(--card-black);
    box-shadow: 0 6px 18px var(--shadow);
    overflow: hidden;
  }
  .card--front { left: 40px; top: 298px; }
  .card--back { left: 620px; top: 298px; }

  .contact {
    position: absolute;
    left: 18px;
    top: 18px;
    font-family: "Didact Gothic", sans-serif;
    color: var(--white);
  }
  .contact__phone {
    font-size: 21px;
    color: var(--blush);
    letter-spacing: 0.5px;
    margin: 0 0 8px;
  }
  .contact__line {
    font-size: 14px;
    margin: 0;
    line-height: 17px;
  }
  .holder-name {
    position: absolute;
    left: 18px;
    top: 222px;
    margin: 0;
    font-family: "Advent Pro", sans-serif;
    font-weight: 200;
    font-size: 36px;
    color: var(--blush);
  }
  .accreditation-seal {
    position: absolute;
    left: 325px;
    top: 104px;
  }
  .tagline-band {
    position: absolute;
    left: 0;
    bottom: 0;
    width: 100%;
    height: 58px;
    background: var(--white);
    display: flex;
    align-items: center;
    justify-content: center;
    gap: 10px;
    font-family: "Didact Gothic", sans-serif;
    font-size: 25px;
    color: var(--band-text);
  }
  .tagline-band svg { display: block; }

  .brand {
    position: absolute;
    inset: 0;
    display: flex;
    align-items: center;
    justify-content: center;
    gap: 14px;
  }
  .brand__mark {
    width: 16px;
    height: 16px;
    border-radius: 50%;
    border: 2px solid var(--blush);
  }
  .brand__name {
    margin: 0;
    font-family: "Didact Gothic", sans-serif;
    font-size: 30px;
    color: var(--blush);
  }
</style>
</head>
<body>
<main class="canvas">
  <section class="card card--front" aria-label="Card front">
    <div class="contact">
      <p class="contact__phone">0452 307 618</p>
      <p class="contact__line">www.tamsinbexley.com.au</p>
      <p class="contact__line">photos@tamsinbexley.com.au</p>
    </div>
    <svg class="accreditation-seal" width="230" height="230" viewBox="0 0 230 230" role="img" aria-label="Coastal Guild of Image Artisans accreditation seal">
      <circle cx="100" cy="100" r="98" fill="var(--card-black)" stroke="var(--white)" stroke-width="3"/>
    </svg>
    <p class="holder-name">Tamsin Bexley</p>
    <div class="tagline-band">
      <svg width="26" height="22" viewBox="0 0 26 22" aria-hidden="true">
        <path d="M13 20 C4 13 1 9 1 6 A5.5 5.5 0 0 1 13 4 A5.5 5.5 0 0 1 25 6 C25 9 22 13 13 20 Z" fill="none" stroke="var(--blush)" stroke-width="1.8"/>
      </svg>
      <span>photos that make your heart skip</span>
    </div>
  </section>

  <section class="card card--back" aria-label="Card back">
    <div class="brand">
      <span class="brand__mark"></span>
      <p class="brand__name">Tamsin Bexley Photography</p>
    </div>
  </section>
</main>
</body>
</html>
```